Quarry IT Services Business Card

Quarry IT Services are a Perth based IT Services company. We would like to incorporate our company logo (attached) and stick with the blue that is in that design. I would like a clean look design that isn't too busy, yet creates a lasting image that is instantly recognisable in the recipients mind.

Target Market(s)

The target audience is small/medium business owners.

Industry/Entity Type

Business

Font styles to use
Serif
Sans Serif

Colors

Designer to choose colors to be used in the design.

Requirements
Must have
• The design should include:
Business name: Quarry IT Services
Directors Name: Darren Mowley
Phone Number: 0462 830 514
Email: support@quarryit.com.au
Website: www.quarryit.com.au

```html
<!DOCTYPE html>
<html lang="en">
<head>
<meta charset="utf-8">
<title>Quarry IT Services Business Card</title>
<link rel="stylesheet" href="https://fonts.googleapis.com/css2?family=Mulish:wght@400;700;800&display=swap">
<style>
  :root {
    --page-bg: #d9d6d1;
    --card-white: #f2f2f2;
    --card-black: #070707;
    --brand-blue: #1e7fe0;
    --brand-light: #3cc3f0;
    --brand-deep: #1452c8;
    --text-dark: #3a3a3a;
    --text-mid: #4a4a4a;
  }
  * { box-sizing: border-box; margin: 0; padding: 0; }
  html, body {
    width: 1200px;
    height: 900px;
    overflow: hidden;
  }
  body {
    background: var(--page-bg);
    font-family: "Mulish", sans-serif;
    display: flex;
    flex-direction: column;
    align-items: center;
    justify-content: center;
    gap: 56px;
  }
  .card {
    width: 580px;
    height: 354px;
    position: relative;
    overflow: hidden;
    box-shadow: 0 8px 24px rgba(0,0,0,0.18);
  }
  .brand {
    display: flex;
    align-items: center;
    gap: 12px;
  }
  .brand-square {
    width: 14px;
    height: 14px;
    background: var(--brand-blue);
  }
  .brand-name {
    font-weight: 800;
    color: var(--brand-blue);
    font-size: 28px;
    letter-spacing: 1px;
  }

  /* Back of card */
  .card-back {
    background: var(--card-black);
    display: flex;
    align-items: center;
    justify-content: center;
  }

  /* Front of card */
  .card-front {
    background: var(--card-white);
  }
  .card-front .brand {
    position: absolute;
    left: 30px;
    top: 34px;
  }
  .card-front .brand-name { font-size: 20px; }
  .brand-graphic {
    position: absolute;
    left: 0;
    top: 84px;
    width: 236px;
    height: 150px;
    background: linear-gradient(135deg, var(--brand-deep) 0%, var(--brand-blue) 40%, var(--brand-light) 100%);
  }
  .contact {
    position: absolute;
    left: 268px;
    top: 118px;
  }
  .contact-name {
    font-weight: 800;
    font-size: 26px;
    color: var(--text-dark);
    margin-bottom: 24px;
    letter-spacing: 0.3px;
  }
  .contact-lines {
    list-style: none;
    font-weight: 400;
    font-size: 16px;
    line-height: 27px;
    color: var(--text-mid);
    letter-spacing: 1.2px;
  }
</style>
</head>
<body>
  <section class="card card-back" aria-label="Card back">
    <div class="brand">
      <span class="brand-square"></span>
      <span class="brand-name">Quarry IT Services</span>
    </div>
  </section>

  <section class="card card-front" aria-label="Card front">
    <div class="brand">
      <span class="brand-square"></span>
      <span class="brand-name">Quarry IT Services</span>
    </div>
    <div class="brand-graphic" role="img" aria-label="Large blue brand graphic area"></div>
    <div class="contact">
      <h1 class="contact-name">Darren Mowley</h1>
      <ul class="contact-lines">
        <li>0462 830 514</li>
        <li>support@quarryit.com.au</li>
        <li>www.quarryit.com.au</li>
      </ul>
    </div>
  </section>
</body>
</html>
```